wolterhagen.info (Physiotherapeut)   //   quellbrand-athletic Webseite
wolterhagen.info (Physiotherapeut) // quellbrand-athletic Webseite
Zielgruppe
Die angesprochene Zielgruppe ist sportlich unterwegs (Sportler jeglicher Sportrichtung). Der externe Shop geht in Richtung Apparels / Kleidung.
Vielleicht wird es aber auch nur eine Physio-Seite und die Apparels kommen im zweiten Schritt - das liegt am Design das man mir präsentiert .... Also legt los ...
(KELVARO wird HOST)
Aufgabenstellung
Mein Name ist Jonathan Wolterhagen ich bin Physiotherapeut / Osteopath (etc).
Die Domain www.wolterhagen.info gehört mir und es würde auch für den Anfang reichen eine digitale Visitenkarte von mir zu erstellen ...
Weiter möchte ich eine Webseite mit dem Namen "quellbrand-athletic" eröffnen. [COM/DE]
Die zu kreierenden Seiten innerhalb der Domain quellbrand-athleti sind:
Main-/LandingPage,
ShopPage (Weiterleitung zu einer externen Webseite),
Impressum,
KooperationsPage (andere Projekte bzw. Webseiten von mir, die in Zukunft kommen).
Design-Vorschläge und umsetzbare / hochladbare Pages (KELVARO) oder NUR Grafiken sind gerne gesehen ...
Die angesprochene Zielgruppe ist sportlich unterwegs (Sportler jeglicher Sportrichtung). Der externe Shop geht in Richtung Apparels.
Die angesprochenen Kreaturen brauchen ein Heim, dass durch ein Schloss repräsentiert werden soll. Evtl. ein Labor. Nicht zu kindlich! Nicht zu düster oder blutig.
Was ich möchte ist: Corporate Identity, eine Webpage (host der Domain wird KELVARO), Logo, etc
Zweiter Schritt wird sein: Grafiken für die Apparels / Klamotten.

```html
<!DOCTYPE html>
<html lang="en">
<head>
<meta charset="utf-8">
<title>Wolterhagen – Physical Therapy</title>
<link href="https://fonts.googleapis.com/css2?family=Roboto+Condensed:wght@400&family=PT+Sans:wght@400;700&display=swap" rel="stylesheet">
<style>
:root{
  --body-grey:#7b7b7b;
  --body-grey-dark:#6e6e6e;
  --text-white:#ffffff;
  --text-dark:#2b2b2b;
  --nav-text:#4a4a4a;
  --info-text:#555555;
  --accent:#9a4f1f;
  --accent-dark:#4a2a17;
  --footer-text:#b9b9b9;
  --footer-faint:#999999;
  --link-blue:#1a1aff;
}
*{margin:0;padding:0;box-sizing:border-box}
html,body{width:1200px;height:1145px;overflow:hidden}
body{position:relative;background:linear-gradient(180deg,var(--body-grey) 0%,var(--body-grey-dark) 100%);font-family:"PT Sans",sans-serif;color:var(--text-white)}
.site-header{position:absolute;left:0;top:0;width:1200px;height:234px;
  background:linear-gradient(90deg,#e6e3de 0%,#d8cfc4 30%,#e9ecef 55%,#dcdfe2 75%,#c9c7c4 100%)}
.brand{position:absolute;left:181px;top:60px;display:flex;align-items:center;gap:11px}
.brand-dot{width:72px;height:72px;border-radius:50%;background:var(--accent)}
.brand-name{font-family:"Roboto Condensed",sans-serif;font-size:33px;color:var(--text-dark);letter-spacing:.3px}
.main-nav{position:absolute;left:0;top:181px;width:600px;height:22px}
.main-nav a{position:absolute;top:0;font-family:"Roboto Condensed",sans-serif;font-size:14px;color:var(--nav-text);text-decoration:none}
.nav-line{position:absolute;left:0;top:200px;width:600px;height:2px;background:linear-gradient(90deg,var(--accent) 0%,var(--accent-dark) 100%)}
.portrait{position:absolute;left:682px;top:0;width:182px;height:234px;
  background:linear-gradient(180deg,#b98f74 0%,#a47b62 45%,#3f90b9 70%,#2f7fae 100%)}
.practice-info{position:absolute;left:880px;top:48px;font-family:"Roboto Condensed",sans-serif;color:var(--info-text);font-size:13px;line-height:17px}
.practice-info .person{margin-bottom:6px}
.lang-btn{position:absolute;left:966px;top:160px;width:55px;height:14px;background:#3a3a3a;color:#fff;font-size:7.5px;line-height:14px;padding-left:25px}
.lang-btn::before{content:"";position:absolute;left:3px;top:3px;width:16px;height:8px;background:#9aa3b8}
.follow{position:absolute;display:flex;align-items:center;gap:3px;font-size:6.5px}
.follow .label{margin-right:4px}
.follow .sq{width:12px;height:12px;border-radius:2px}
.header-follow{left:926px;top:191px;color:#444}
.header-follow .sq{background:#5d6f8a}
.intro{position:absolute;left:182px;top:276px;width:419px;font-size:13.5px;line-height:16.3px;text-align:justify;hyphens:auto;-webkit-hyphens:auto}
.intro p{margin-bottom:16px}
.news{position:absolute;left:688px;top:283px;width:332px}
.news h2{font-size:13px;font-weight:700;line-height:16px;margin-bottom:3px}
.news p{font-size:8.1px;line-height:10.8px;text-align:justify;hyphens:auto;-webkit-hyphens:auto;margin-bottom:18px}
.sports-grid{position:absolute;left:2px;top:589px;width:1198px;height:350px}
.tile{position:absolute}
.site-footer{position:absolute;left:0;top:1040px;width:1200px;height:105px;font-size:7.5px}
.footer-nav{position:absolute;left:333px;top:3px;list-style:none}
.footer-nav li{height:16px;color:var(--footer-text)}
.copyright{position:absolute;left:433px;top:3px;width:335px;color:var(--footer-text);font-size:5.7px;line-height:8px}
.copyright div{white-space:nowrap}
.contact{position:absolute;left:785px;top:2px;color:var(--footer-faint);font-size:7.5px;line-height:11px}
.contact a{color:var(--link-blue);text-decoration:underline}
.footer-follow{left:785px;top:1100px;color:var(--footer-faint)}
.footer-follow .sq{background:#6b83a8}
</style>
</head>
<body>
<header class="site-header">
  <div class="brand"><span class="brand-dot"></span><span class="brand-name">Wolterhagen</span></div>
  <nav class="main-nav">
    <a style="left:182px">Main</a>
    <a style="left:270px">News</a>
    <a style="left:356px">Shop</a>
    <a style="left:437px">Contacts</a>
    <a style="left:530px">Cooperation</a>
  </nav>
  <div class="nav-line"></div>
  <div class="portrait" role="img" aria-label="Portrait photo of the physiotherapist in a blue polo shirt"></div>
  <div class="practice-info">
    <div class="person">Jonathan Wolterhagen</div>
    <div>Physical Therapy</div>
    <div>Osteopathic Medicine</div>
  </div>
  <div class="lang-btn">English</div>
  <div class="follow header-follow"><span class="label">Follow Us</span><span class="sq"></span><span class="sq"></span><span class="sq"></span><span class="sq"></span></div>
</header>

<section class="intro">
  <p>Lorem ipsum dolor sit amet, consectetur adipiscing elit, sed do eiusmod tempor incididunt ut labore et dolore magna aliqua. Ut enim ad minim veniam, quis nostrud exercitation ullamco laboris nisi ut aliquip ex ea commodo consequat. Duis aute irure dolor in reprehenderit in voluptate velit esse cillum dolore eu fugiat nulla pariatur. Excepteur sint occaecat cupidatat non proident, sunt in culpa qui officia deserunt mollit anim id est laborum.</p>
  <p>Lorem ipsum dolor sit amet, consectetur adipiscing elit, sed do eiusmod tempor incididunt ut labore et dolore magna aliqua. Ut enim ad minim veniam, quis nostrud exercitation ullamco laboris nisi ut aliquip ex ea commodo consequat. Duis aute irure dolor in reprehenderit in voluptate velit esse cillum dolore eu fugiat nulla pariatur. Excepteur sint occaecat cupidatat non proident, sunt in culpa qui officia deserunt mollit anim id est laborum.</p>
</section>

<aside class="news">
  <h2>Latest News</h2>
  <p>Lorem ipsum dolor sit amet, consectetur adipiscing elit, sed do eiusmod tempor incididunt ut labore et dolore magna aliqua. Ut enim ad minim veniam, quis nostrud exercitation ullamco laboris nisi ut aliquip ex ea commodo consequat. Duis aute irure dolor in reprehenderit in voluptate velit esse cillum dolore eu fugiat nulla pariatur. Excepteur sint occaecat cupidatat non proident, sunt in culpa qui officia deserunt mollit anim id est laborum.</p>
  <h2>Latest News</h2>
  <p>Lorem ipsum dolor sit amet, consectetur adipiscing elit, sed do eiusmod tempor incididunt ut labore et dolore magna aliqua. Ut enim ad minim veniam, quis nostrud exercitation ullamco laboris nisi ut aliquip ex ea commodo consequat. Duis aute irure dolor in reprehenderit in voluptate velit esse cillum dolore eu fugiat nulla pariatur. Excepteur sint occaecat cupidatat non proident, sunt in culpa qui officia deserunt mollit anim id est laborum. Lorem ipsum dolor sit amet, consectetur adipiscing elit, sed do eiusmod tempor incididunt ut labore et dolore magna aliqua. Ut enim ad minim veniam, quis nostrud exercitation ullamco laboris nisi ut aliquip ex ea commodo consequat. Duis aute irure dolor in reprehenderit in voluptate velit esse cillum dolore eu fugiat nulla pariatur. Excepteur sint</p>
</aside>

<section class="sports-grid">
  <div class="tile" style="left:0;top:0;width:279px;height:186px;background:linear-gradient(135deg,#2a323a,#3f4a55)" role="img" aria-label="Basketball player dunking, blue-toned photo"></div>
  <div class="tile" style="left:279px;top:0;width:307px;height:186px;background:linear-gradient(135deg,#5c7180,#a9bcc8)" role="img" aria-label="Skier carving through snow, blue-toned photo"></div>
  <div class="tile" style="left:586px;top:0;width:253px;height:186px;background:linear-gradient(135deg,#8ea3b1,#6f8594)" role="img" aria-label="Two ice hockey players, blue-toned photo"></div>
  <div class="tile" style="left:839px;top:0;width:359px;height:186px;background:linear-gradient(135deg,#6f8594,#56697a)" role="img" aria-label="Tennis player hitting a ball, blue-toned photo"></div>
  <div class="tile" style="left:0;top:186px;width:279px;height:164px;background:linear-gradient(135deg,#a3b5c1,#6f8594)" role="img" aria-label="Two athletes stretching, blue-toned photo"></div>
  <div class="tile" style="left:279px;top:186px;width:219px;height:164px;background:linear-gradient(135deg,#3f4a55,#687c8a)" role="img" aria-label="Footballer kicking a ball, blue-toned photo"></div>
  <div class="tile" style="left:498px;top:186px;width:246px;height:164px;background:linear-gradient(180deg,#7e94a3,#3f5060)" role="img" aria-label="Swimmer underwater, blue-toned photo"></div>
  <div class="tile" style="left:744px;top:186px;width:230px;height:164px;background:linear-gradient(180deg,#8ea3b1,#4f6170)" role="img" aria-label="Runner on a beach, blue-toned photo"></div>
  <div class="tile" style="left:974px;top:186px;width:224px;height:164px;background:linear-gradient(135deg,#7a909f,#556674)" role="img" aria-label="Two athletes in sprint start position, blue-toned photo"></div>
</section>

<footer class="site-footer">
  <ul class="footer-nav">
    <li>Main</li><li>News</li><li>Shop</li><li>Contacts</li><li>Cooperation</li>
  </ul>
  <div class="copyright">
    <div>Copyright information. Copyright information. Copyright information. Copyright information. Copyright information.</div>
    <div>Copyright information. Copyright information. Copyright information. Copyright information. Copyright information.</div>
    <div>Copyright information. Copyright information. Copyright information. Copyright information. Copyright information.</div>
    <div>Copyright information. Copyright information. Copyright information. Copyright information. Copyright information.</div>
    <div>Copyright information. Copyright information. Copyright information. Copyright information. Copyright information.</div>
    <div>Copyright information. Copyright information. Copyright information. Copyright information. Copyright information.</div>
    <div>Copyright information. Copyright information. Copyright information. Copyright information. Copyright information.</div>
    <div>Copyright information. Copyright information. Copyright information. Copyright information. Copyright information.</div>
    <div>Copyright information. Copyright information. Copyright information. Copyright information. Copyright information.</div>
  </div>
  <div class="contact">
    Contact Us<br>
    Lindenweg 14/15<br>
    26135 Brelingen<br>
    Tel.: +49 (0)400 555 010<br>
    E-mail: <a>info@wolterhagen.info</a>
  </div>
</footer>
<div class="follow footer-follow"><span class="label">Follow Us</span><span class="sq"></span><span class="sq"></span><span class="sq"></span><span class="sq"></span></div>
</body>
</html>
```